Creative, fresh business card design for Brindlecrest Linings

We need a fresh, creative business card design for Brindlecrest Linings. We are the manufacturer of Brindlecrest Linings in Australia. Wall panels are 2400 x 1200mm panels made from MDF and feature 3D patterns on the face of the panel. The colours to be used are green, silver/grey and white RGB
Red 187
Green 207
Blue 65.

An idea is to possibly use a watermark of one of our designs as a background (like on the "Lattice" design on the left hand side of page 2 of our brochure).

Target Market(s)

Interior designers, architects, builders and home renovators

Industry/Entity Type

Business

Contact Information for Business Card

Details to go on the card are:
Our logo (attached),
Slogan: "Decorative panels for interiors and exteriors",
Contact name,
Position,
Mobile phone number,
Business address,
Business phone,
Business fax,
Website and
Email address.

I have attached a few images of our panels and our brochure for reference.

The colours of the business card should feature our logo colours which are: RGB
Red 187
Green 207
Blue 65

Requirements
Must have
• Very modern fonts and design. Some of the designs shown especially the "Weave" design which is a popular design.
Nice to have
• Creative but simple design. Very contemporary.
Should not have
• Anything ornate or old fashioned.

```html
<!DOCTYPE html>
<html lang="en">
<head>
<meta charset="utf-8">
<title>Brindlecrest Linings – Business Card</title>
<link rel="stylesheet" href="https://fonts.googleapis.com/css2?family=Roboto:wght@700&family=Source+Sans+3:wght@400;600&display=swap">
<style>
  :root {
    --green: #bccf41;
    --grey: #8e8e8e;
    --ink: #1e1e1e;
    --paper: #ffffff;
    --paper-shade: #f2f2f2;
    --backdrop: #e6e6e4;
  }
  * { margin: 0; padding: 0; box-sizing: border-box; }
  html, body {
    width: 1200px; height: 900px; overflow: hidden;
    background: var(--backdrop);
    font-family: "Source Sans 3", sans-serif;
  }
  .card {
    position: absolute; left: 111px; top: 148px;
    width: 978px; height: 603px;
    background: linear-gradient(180deg, var(--paper) 0%, var(--paper-shade) 100%);
    box-shadow: 0 10px 30px rgba(0,0,0,.15);
    overflow: hidden;
  }
  .pattern-panel {
    position: absolute; left: 558px; top: 0; width: 420px; height: 503px;
    background: linear-gradient(135deg, #f7f7f7 0%, #e4e4e4 45%, #f1f1f1 70%, #dcdcdc 100%);
  }
  .brand {
    position: absolute; left: 57px; top: 54px;
    display: flex; align-items: center; gap: 22px;
  }
  .brand-square { width: 118px; height: 118px; background: var(--green); }
  .brand-name {
    font-family: "Source Sans 3", sans-serif; font-weight: 600;
    font-size: 50px; line-height: 1.02; color: var(--grey);
  }
  .tagline {
    position: absolute; left: 57px; top: 296px; width: 400px;
    font-size: 23px; line-height: 30px; letter-spacing: 3.4px;
    color: var(--grey); text-align: center;
  }
  .contact {
    position: absolute; left: 54px; top: 378px;
    font-size: 25px; color: var(--ink); line-height: 38px;
  }
  .contact-row { display: flex; white-space: nowrap; }
  .contact-row .label { color: var(--green); font-weight: 600; margin-right: 6px; }
  .contact-row .gap { width: 28px; }
  .contact-row .web { color: var(--green); font-weight: 600; margin-left: 26px; }
  .person {
    position: absolute; right: 60px; top: 80px; text-align: right;
  }
  .person-name {
    font-family: "Roboto", sans-serif; font-weight: 700;
    font-size: 34px; letter-spacing: 1.5px; color: var(--green);
  }
  .person-role { font-size: 25px; color: var(--ink); margin-top: 4px; }
  .address-band {
    position: absolute; left: 0; top: 503px; width: 978px; height: 100px;
    background: var(--green);
    display: flex; align-items: center; padding-left: 56px;
    font-size: 25px; color: var(--paper);
  }
</style>
</head>
<body>
  <div class="card">
    <div class="pattern-panel" role="img" aria-label="Faint embossed 3D wall panel pattern of grey pyramids"></div>

    <div class="brand">
      <div class="brand-square"></div>
      <div class="brand-name">Brindlecrest<br>Linings</div>
    </div>

    <p class="tagline">decorative panels for interiors &amp; landscapes</p>

    <div class="contact">
      <div class="contact-row"><span class="label">P:</span>(061) 482 730 915<span class="gap"></span><span class="label">M:</span>&nbsp;(061)497215836</div>
      <div class="contact-row"><span class="label">E:</span>&nbsp;hello@brindlecrest.au<span class="web">www.brindlecrest.au</span></div>
    </div>

    <div class="person">
      <div class="person-name">MARA ELLISON</div>
      <div class="person-role">Managing Director</div>
    </div>

    <div class="address-band">27, Harlow Lane, Ferndale Vale, Australia, 4821</div>
  </div>
</body>
</html>
```